Visitenkarte erstellen für Reiki Praxis

Visitenkarten für Reiki Praxis Doppelseitig

business cards reiki practice double-sided

The background can also be a different color

```html
<!DOCTYPE html>
<html lang="en">
<head>
<meta charset="utf-8">
<title>Lichtquelle – Business Cards</title>
<link rel="stylesheet" href="https://fonts.googleapis.com/css2?family=Montserrat:wght@400;500;600&display=swap">
<style>
  :root {
    --backdrop: #8a6f52;
    --card-white: #ffffff;
    --card-dark: #1c1c1c;
    --card-purple: #7a5ba6;
    --gold: #e3a82a;
    --ink: #111111;
    --light-text: #f2f2f2;
  }
  * { margin: 0; padding: 0; box-sizing: border-box; }
  html, body {
    width: 900px; height: 1200px; overflow: hidden;
    background: var(--backdrop);
    font-family: "Montserrat", sans-serif;
  }
  .canvas { position: relative; width: 900px; height: 1200px; }

  .card {
    position: absolute; left: 80px; width: 742px; height: 440px;
    border-radius: 30px; overflow: hidden;
    box-shadow: 0 6px 14px rgba(0,0,0,0.45);
  }
  .card--front { top: 132px; background: var(--card-white); }
  .card--back { top: 638px; background: var(--card-purple); }

  /* front: brand area */
  .brand-mark {
    position: absolute; left: 144px; top: 38px;
    width: 62px; height: 62px; border-radius: 50%;
    border: 2px solid var(--gold);
  }
  .brand-name {
    position: absolute; left: 0; width: 348px; text-align: center;
    font-weight: 500; color: var(--ink); text-transform: uppercase;
  }
  .brand-name--primary { left: 34px; top: 152px; font-size: 35px; letter-spacing: 0.5px; }
  .brand-name--secondary { left: 34px; top: 192px; font-size: 26px; letter-spacing: 4px; }

  /* front: contact band */
  .contact-band {
    position: absolute; left: 0; top: 250px; width: 100%; height: 190px;
    background: var(--card-dark); color: var(--light-text);
  }
  .person-name {
    position: absolute; left: 33px; top: 10px;
    font-size: 22px; font-weight: 600; color: var(--gold);
  }
  .person-role { position: absolute; left: 35px; top: 42px; font-size: 15px; }
  .contact-list { position: absolute; left: 35px; top: 82px; list-style: none; }
  .contact-list li {
    display: flex; align-items: center; height: 26.5px; font-size: 16px;
  }
  .contact-list svg { width: 14px; height: 14px; margin-right: 16px; fill: var(--gold); }
  .address {
    position: absolute; left: 534px; top: 116px;
    font-size: 16px; line-height: 20px; font-style: normal;
  }

  /* back */
  .back-mark {
    position: absolute; left: 340px; top: 80px;
    width: 62px; height: 62px; border-radius: 50%;
    border: 2px solid var(--gold);
  }
  .back-name {
    position: absolute; left: 0; width: 100%; text-align: center;
    color: var(--gold); font-weight: 500; text-transform: uppercase;
  }
  .back-name--primary { top: 256px; font-size: 52px; letter-spacing: 1px; }
  .back-name--secondary { top: 316px; font-size: 38px; letter-spacing: 6px; }
</style>
</head>
<body>
<main class="canvas">

  <section class="card card--front" aria-label="Business card front">
    <span class="brand-mark"></span>
    <p class="brand-name brand-name--primary">Lichtquelle</p>
    <p class="brand-name brand-name--secondary">Mara Lindt</p>

    <div class="contact-band">
      <h1 class="person-name">Mara Lindt</h1>
      <p class="person-role">CEO &amp; Founder</p>
      <ul class="contact-list">
        <li>
          <svg viewBox="0 0 24 24" aria-hidden="true"><path d="M6.6 10.8a15.1 15.1 0 0 0 6.6 6.6l2.2-2.2a1 1 0 0 1 1-.25 11.4 11.4 0 0 0 3.6.57 1 1 0 0 1 1 1V20a1 1 0 0 1-1 1A17 17 0 0 1 3 4a1 1 0 0 1 1-1h3.5a1 1 0 0 1 1 1c0 1.25.2 2.45.57 3.57a1 1 0 0 1-.25 1z"/></svg>
          1-800-555-0142
        </li>
        <li>
          <svg viewBox="0 0 24 24" aria-hidden="true"><path d="M2 6h20v2l-10 6L2 8z M2 10l10 6 10-6v8H2z"/></svg>
          info@yourmail.com
        </li>
        <li>
          <svg viewBox="0 0 24 24" aria-hidden="true"><path d="M12 2a10 10 0 1 0 0 20 10 10 0 0 0 0-20zm-1 17.9A8 8 0 0 1 4.1 11H7l2 2v2l2 2zM17.9 16.4A2 2 0 0 0 16 15h-1v-3H9v-2h2l1-3h2a8 8 0 0 1 3.9 9.4z"/></svg>
          www.yourwebsite.com
        </li>
      </ul>
      <address class="address">14 Maple Court<br>Harwood NY 10452</address>
    </div>
  </section>

  <section class="card card--back" aria-label="Business card back">
    <span class="back-mark"></span>
    <p class="back-name back-name--primary">Lichtquelle</p>
    <p class="back-name back-name--secondary">Mara Lindt</p>
  </section>

</main>
</body>
</html>
```